Business card design needed

Business Card design required for new small plumbing business.
Would like a logo/text look that is simple and unique and does not have to be representative of a plumbing company (ie. having a cartoon plumber or toilet etc) as the companyname is self explanatory.
Would like the main colour to be green (lime green).
Updates

Industry/Entity Type

Plumber

Contact Information for Business Card

BRAVELL PLUMBING
ABN 61 904 127 558 003

Trevor Hasketh
Licensed Plumber 83615
Phone: 0412 870 245

27 Bravell Drive,
Kestrel Vale. 3987 Westmarch

Email: bravellplumbing@mailnest.example

Logo Text

Bravell Plumbing

Logo styles of interest
Character Logo
Wordmark Logo
Lettermark Logo

```html
<!DOCTYPE html>
<html lang="en">
<head>
<meta charset="utf-8">
<title>Bravell Plumbing – Business Card</title>
<link rel="stylesheet" href="https://fonts.googleapis.com/css2?family=Marcellus&family=Noto+Sans:wght@500&display=swap">
<style>
  :root {
    --border-blue: #2d4f97;
    --card-green: #22aa3a;
    --edge-green: #8fd36a;
    --mark-white: #ffffff;
    --rule-dark: #1a1a1a;
    --contact-yellow: #f4f400;
  }
  html, body {
    margin: 0;
    padding: 0;
    width: 1200px;
    height: 743px;
    overflow: hidden;
    background: #ffffff;
  }
  .card {
    position: relative;
    width: 1200px;
    height: 743px;
    box-sizing: border-box;
    background: var(--border-blue);
    padding: 11px;
  }
  .card-face {
    position: relative;
    width: 100%;
    height: 100%;
    box-sizing: border-box;
    background: var(--card-green);
    border: 2px solid var(--edge-green);
    overflow: hidden;
  }
  .brand {
    position: absolute;
    left: 0;
    top: 0;
    width: 1174px;
    height: 470px;
  }
  .brand-name {
    font-family: "Marcellus", serif;
    font-size: 104px;
    fill: var(--mark-white);
  }
  .brand-dot {
    fill: var(--mark-white);
  }
  .brand-rule {
    fill: var(--mark-white);
    stroke: var(--rule-dark);
    stroke-width: 1.2;
  }
  .contact {
    position: absolute;
    left: 111px;
    top: 545px;
    margin: 0;
    font-family: "Noto Sans", sans-serif;
    font-weight: 500;
    font-size: 30px;
    line-height: 33px;
    color: var(--contact-yellow);
    white-space: pre;
  }
  .contact-line {
    display: block;
  }
</style>
</head>
<body>
  <div class="card">
    <div class="card-face">
      <svg class="brand" viewBox="0 0 1174 470" aria-label="Bravell Plumbing">
        <circle class="brand-dot" cx="584" cy="232" r="40"/>
        <text class="brand-name" x="122" y="392" textLength="936" lengthAdjust="spacingAndGlyphs">BRAVELL PLUMBING</text>
        <rect class="brand-rule" x="122" y="408" width="936" height="6"/>
      </svg>
      <p class="contact"><span class="contact-line">ABN  61 904 127 558 003 Trevor Hasketh Licensed Plumber 83615</span><span class="contact-line">Phone: 0412 870 245  27 Bravell Drive, Kestrel Vale. 3987 Westmarch</span><span class="contact-line">Email: bravellplumbing@mailnest.example</span></p>
    </div>
  </div>
</body>
</html>
```